43 Year Old Construction firm needs Updated Business Card & Stationery Design

We are an established and well known (in our market) commercial construction firm. We need a cleaner and more modern look for our corporate identity material. We would like to continue to use our current colors and logo.
We are thinking about incorporating a slogan on our business card (either front or back): "Striving to be the most trusted builder in our market." The text could change at some point. Our website is www.kradworth.example . Sample card is attached. Some will have more phone numbers, etc...
Updates

Target Market(s)

Commercial and institutional clients.

Industry/Entity Type

Construction Company

Contact Information for Business Card

See attached for existing card. But don't be constrained.

Requirements
Must have
• Logo, name, title, address, website, email, phone numbers (as few as one, as many as three)
• Slogan on front or back "Striving to be the most trusted builder in our market"
• Use existing logo and colors

```html
<!DOCTYPE html>
<html lang="en">
<head>
<meta charset="utf-8">
<title>Kradworth Constructors – Business Card</title>
<link rel="stylesheet" href="https://fonts.googleapis.com/css2?family=Open+Sans:wght@400;600;700&display=swap">
<style>
  :root {
    --brand-blue: #0b4588;
    --ink-blue: #173f82;
    --brand-green: #0a9d4f;
    --card-white: #ffffff;
    --backdrop: #e8e9ec;
  }
  * { margin: 0; padding: 0; box-sizing: border-box; }
  html, body {
    width: 1200px;
    height: 900px;
    overflow: hidden;
    background: var(--backdrop);
    font-family: "Open Sans", Arial, sans-serif;
  }
  .business-card {
    position: absolute;
    left: 80px;
    top: 129px;
    width: 1040px;
    height: 642px;
    background: var(--card-white);
    overflow: hidden;
    box-shadow: 0 6px 24px rgba(0, 0, 0, 0.12);
  }
  .card-wave {
    position: absolute;
    inset: 0;
    width: 100%;
    height: 100%;
  }
  .wordmark {
    position: absolute;
    left: 118px;
    top: 150px;
    color: var(--card-white);
    font-weight: 700;
    line-height: 1;
  }
  .wordmark-name {
    display: block;
    font-size: 68px;
    letter-spacing: 1px;
  }
  .wordmark-trade {
    display: block;
    margin-top: 34px;
    font-size: 26px;
    letter-spacing: 5.4px;
  }
  .contact-block {
    position: absolute;
    right: 26px;
    top: 0;
    text-align: right;
    color: var(--ink-blue);
  }
  .person-name {
    position: absolute;
    right: 0;
    top: 278px;
    white-space: nowrap;
    font-size: 34px;
    font-weight: 600;
  }
  .person-title {
    position: absolute;
    right: 0;
    top: 323px;
    white-space: nowrap;
    font-size: 26px;
  }
  .address {
    position: absolute;
    right: 0;
    top: 385px;
    white-space: nowrap;
    font-size: 26px;
    line-height: 37px;
  }
  .contact-lines {
    position: absolute;
    right: 0;
    top: 486px;
    list-style: none;
    font-size: 26px;
    line-height: 37.5px;
  }
  .contact-lines li {
    display: flex;
    justify-content: flex-end;
    align-items: center;
    white-space: nowrap;
    gap: 16px;
  }
  .contact-icon {
    width: 20px;
    height: 20px;
    fill: var(--ink-blue);
    flex: none;
  }
</style>
</head>
<body>
  <div class="business-card">
    <svg class="card-wave" viewBox="0 0 652 402" preserveAspectRatio="none" aria-hidden="true">
      <path fill="var(--brand-blue)" d="M0 0 H652 V176 C640 154 600 114 540 124 C420 144 300 304 200 318 C130 328 60 304 0 224 Z"/>
      <path fill="var(--brand-green)" d="M0 0 H652 V170 C640 148 600 108 540 119 C420 138 300 299 200 312 C130 322 60 298 0 219 Z"/>
      <path fill="var(--brand-blue)" d="M0 0 H652 V160 C640 140 600 100 540 110 C420 130 300 290 200 305 C130 315 60 290 0 210 Z"/>
    </svg>

    <div class="wordmark">
      <span class="wordmark-name">KRADWORTH</span>
      <span class="wordmark-trade">CONSTRUCTORS</span>
    </div>

    <div class="contact-block">
      <p class="person-name">Marcus Ellery</p>
      <p class="person-title">Managing Director</p>
      <p class="address">4870 Fenwick Road, Suite 12<br>Halden County, 604218.</p>
      <ul class="contact-lines">
        <li>044-555 018 274
          <svg class="contact-icon" viewBox="0 0 24 24" aria-hidden="true"><path d="M6.6 10.8a15.2 15.2 0 0 0 6.6 6.6l2.2-2.2c.3-.3.7-.4 1-.2 1.1.4 2.3.6 3.6.6.6 0 1 .4 1 1V20c0 .6-.4 1-1 1A17 17 0 0 1 3 4c0-.6.4-1 1-1h3.5c.6 0 1 .4 1 1 0 1.3.2 2.5.6 3.6.1.3 0 .7-.2 1z"/></svg>
        </li>
        <li>office@kradworth.example
          <svg class="contact-icon" viewBox="0 0 24 24" aria-hidden="true"><path d="M3 5h18v14H3z"/><path d="M4.5 7 12 12.5 19.5 7" fill="none" stroke="#fff" stroke-width="1.4"/></svg>
        </li>
        <li>www.kradworth.example
          <svg class="contact-icon" viewBox="0 0 24 24" aria-hidden="true"><circle cx="12" cy="12" r="10"/><path d="M2 12h20M12 2c3 3 3 17 0 20M12 2c-3 3-3 17 0 20" fill="none" stroke="#fff" stroke-width="1.4"/></svg>
        </li>
      </ul>
    </div>
  </div>
</body>
</html>
```